Looking for a new business card design

We are looking for a corporate looking yet still a bit different then the rest. I would like the card black with the picture on the back and the phrase "Lighting the way to safer sites" on the back as well. Then a clean look on the front with a bit of an edge.

Target Market(s)

Corporate oil executives and drilling supervisors

Industry/Entity Type

Oil And Gas

Contact Information for Business Card

Black, bold, clean lines.

Font styles to use
Sans Serif

Requirements
Must have
• Picture on the back with the slogan "Lighting the way to safer sites"
• Black background
• Stands out

```html
<!DOCTYPE html>
<html lang="en">
<head>
<meta charset="utf-8">
<title>Helios Energy Services Corp. – Business Card</title>
<link rel="stylesheet" href="https://fonts.googleapis.com/css2?family=Source+Sans+3:ital,wght@0,400;0,600;0,700;1,700&display=swap">
<style>
  :root {
    --page-bg: #e9e7e4;
    --card-white: #ffffff;
    --card-black: #050505;
    --ink-blue: #3a6591;
    --accent-green: #a9c11f;
    --text-grey: #555a5f;
    --muted-grey: #8c8f92;
    --white: #ffffff;
  }
  * { box-sizing: border-box; margin: 0; padding: 0; }
  html, body {
    width: 1200px; height: 987px; overflow: hidden;
    background: var(--page-bg);
    font-family: "Source Sans 3", Arial, sans-serif;
  }
  .sheet { position: relative; width: 1200px; height: 987px; }
  .card {
    position: absolute; left: 292px; width: 615px; height: 352px;
    box-shadow: 0 3px 10px rgba(0,0,0,.25);
    overflow: hidden;
  }
  /* Front */
  .card-front { top: 131px; background: var(--card-white); }
  .edge-bar { position: absolute; left: 0; top: 76px; width: 12px; height: 42px; background: var(--card-black); }
  .holder-name { position: absolute; left: 40px; top: 72px; font-size: 22px; font-weight: 700; color: var(--ink-blue); letter-spacing: .3px; }
  .holder-role { position: absolute; left: 40px; top: 100px; font-size: 17px; color: var(--accent-green); }
  .address { position: absolute; left: 40px; top: 126px; font-size: 16px; line-height: 23px; color: var(--text-grey); }
  .contact-list { position: absolute; left: 40px; top: 180px; list-style: none; }
  .contact-list li { display: flex; align-items: center; height: 23.5px; font-size: 16px; color: var(--text-grey); }
  .contact-list svg { width: 15px; height: 15px; margin-right: 10px; fill: var(--ink-blue); flex: none; }
  .brand-lockup { position: absolute; left: 372px; top: 228px; display: flex; align-items: center; }
  .brand-dot { width: 54px; height: 54px; border-radius: 50%; background: var(--ink-blue); margin-right: 16px; }
  .brand-name { font-size: 35px; font-weight: 600; color: var(--accent-green); line-height: 1; }
  .brand-sub { font-size: 14px; color: var(--muted-grey); margin-top: 2px; }
  /* Back */
  .card-back { top: 503px; background: var(--card-black); }
  .site-photo {
    position: absolute; left: 175px; top: 0; right: 0; bottom: 0;
    background:
      radial-gradient(ellipse 42% 38% at 50% 52%, #b9a98a 0%, #8f8568 35%, #3d4330 65%, rgba(10,12,8,0) 100%),
      linear-gradient(180deg, #0b0c0a 0%, #16190f 60%, #0a0b08 100%);
  }
  .vertical { position: absolute; writing-mode: vertical-rl; transform: rotate(180deg); white-space: nowrap; }
  .back-name { left: 64px; bottom: 166px; font-size: 37px; font-weight: 600; color: var(--accent-green); line-height: 1; }
  .back-sub { left: 103px; bottom: 166px; font-size: 14px; color: var(--muted-grey); line-height: 1; }
  .slogan { left: 140px; bottom: 30px; font-size: 21px; font-weight: 700; font-style: italic; color: var(--white); line-height: 1; }
  .back-dot { position: absolute; left: 44px; top: 226px; width: 74px; height: 74px; border-radius: 50%; background: var(--white); }
</style>
</head>
<body>
<div class="sheet">
  <section class="card card-front">
    <div class="edge-bar"></div>
    <h1 class="holder-name">MARA KESSLING</h1>
    <p class="holder-role">CEO/Founder</p>
    <p class="address">4120 Tundra Ridge Road<br>Fairbanks, Alaska 99712</p>
    <ul class="contact-list">
      <li><svg viewBox="0 0 16 16"><path d="M3.2 1.2l2.4-.4 1.4 3.2-1.6 1.2a9 9 0 0 0 5.4 5.4l1.2-1.6 3.2 1.4-.4 2.4c-.2.9-1 1.4-1.9 1.3C6.7 13.5 2.5 9.3 1.9 3.1c-.1-.9.4-1.7 1.3-1.9z"/></svg>907 555 0142</li>
      <li><svg viewBox="0 0 16 16"><path d="M4.5 0h7A1.5 1.5 0 0 1 13 1.5v13a1.5 1.5 0 0 1-1.5 1.5h-7A1.5 1.5 0 0 1 3 14.5v-13A1.5 1.5 0 0 1 4.5 0zM5 2v10h6V2zm3 11a1 1 0 1 0 0 2 1 1 0 0 0 0-2z"/></svg>907 555 0178</li>
      <li><svg viewBox="0 0 16 16"><path d="M4 1h8v4H4zM1 6h14v6h-2v3H3v-3H1zm4 4v3h6v-3z"/></svg>907 555 0193</li>
      <li><svg viewBox="0 0 16 16"><path d="M1 3h14v1.2L8 9 1 4.2zm0 2.6l7 4.8 7-4.8V13H1z"/></svg>mara@helios.com</li>
      <li><svg viewBox="0 0 16 16"><path d="M8 1a7 7 0 1 0 0 14A7 7 0 0 0 8 1zm0 1.5c.8 0 1.7 1.6 2 4H6c.3-2.4 1.2-4 2-4zM2.6 7.5h2.1a13 13 0 0 0 0 1H2.6zm8.7 0h2.1v1h-2.1zM6 9.5h4c-.3 2.4-1.2 4-2 4s-1.7-1.6-2-4z"/></svg>www.helios.com</li>
    </ul>
    <div class="brand-lockup">
      <div class="brand-dot"></div>
      <div>
        <div class="brand-name">HELIOS</div>
        <div class="brand-sub">Energy Services Corp.</div>
      </div>
    </div>
  </section>

  <section class="card card-back">
    <div class="site-photo" role="img" aria-label="Aerial night photograph of a floodlit drilling rig site surrounded by dark forest"></div>
    <span class="vertical back-name">HELIOS</span>
    <span class="vertical back-sub">Energy Services Corp.</span>
    <span class="vertical slogan">Lighting the way to safer sites</span>
    <div class="back-dot"></div>
  </section>
</div>
</body>
</html>
```